Poly Bag Packaging Motorcycle Cables - Veronzo Brand

Poly Bag Dimensions: 33cm(H) x 24cm(W)
We would like to design a genuine Poly Bag Packaging for motorcycle cables.
Veronzo, is one of the leading companies for manufacturing Motorcycles, located in Egypt. Our company is offering high-quality products, the best in the local market, with very competitive prices.
We have a limited time to get this project done, So we Highly appreciate receiving your designs ASAP.
Target Market(s)
Motorcycle Spare parts Buyers
Font styles to use
Colors
Designer to choose colors to be used in the design.
Look and feel
Each slider illustrates characteristics of the customer's brand and the style your logo design should communicate.

```html
<!DOCTYPE html>
<html lang="en">
<head>
<meta charset="utf-8">
<title>Veronzo Motorcycle Cable Poly Bag</title>
<link href="https://fonts.googleapis.com/css2?family=Audiowide&family=Exo+2:ital,wght@0,400;0,500;1,600&display=swap" rel="stylesheet">
<style>
  :root {
    --stage: #c9cacc;
    --film: #e4e5e7;
    --film-shade: #b9bbbe;
    --red: #d92b34;
    --blue: #2e31a0;
    --yellow: #f5e03a;
    --white: #f3f3f3;
    --ink-grey: #6b6d70;
  }
  html, body {
    margin: 0;
    width: 1200px;
    height: 1200px;
    overflow: hidden;
    background: var(--stage);
  }
  .canvas {
    position: relative;
    width: 1200px;
    height: 1200px;
  }
  .bag {
    position: absolute;
    left: 240px;
    top: 80px;
    width: 720px;
    height: 1040px;
    overflow: hidden;
    box-shadow: 0 10px 30px rgba(0,0,0,0.18);
  }
  .bag__contents {
    position: absolute;
    inset: 0;
    background: radial-gradient(circle at 50% 55%, var(--film) 0%, #d6d7da 55%, var(--film-shade) 100%);
  }
  .bag__print {
    position: absolute;
    inset: 0;
  }
  .banner__title {
    position: absolute;
    left: 23px;
    top: 124px;
    width: 600px;
    margin: 0;
    font-family: "Audiowide", sans-serif;
    font-weight: 400;
    font-size: 46px;
    line-height: 1;
    letter-spacing: 0;
    color: var(--white);
    white-space: nowrap;
  }
  .banner__tagline {
    position: absolute;
    left: 18px;
    top: 176px;
    margin: 0;
    font-family: "Exo 2", sans-serif;
    font-style: italic;
    font-weight: 600;
    font-size: 23px;
    line-height: 1;
    color: var(--white);
    white-space: nowrap;
  }
  .label {
    position: absolute;
    left: 205px;
    top: 807px;
    width: 352px;
    height: 180px;
    border-radius: 14px;
    overflow: hidden;
    background: var(--blue);
  }
  .label__brand {
    height: 63px;
    background: var(--white);
    display: flex;
    align-items: center;
    justify-content: center;
    gap: 10px;
  }
  .label__mark {
    width: 30px;
    height: 30px;
    border-radius: 50%;
    background: var(--ink-grey);
  }
  .label__name {
    font-family: "Audiowide", sans-serif;
    font-size: 30px;
    letter-spacing: 2px;
    color: var(--ink-grey);
  }
  .label__specs {
    margin: 15px 0 0 46px;
    width: 258px;
    border-collapse: collapse;
    font-family: "Exo 2", sans-serif;
    font-size: 15px;
    color: var(--white);
  }
  .label__specs td {
    border: 1.5px solid var(--white);
    height: 20px;
    padding: 0;
    text-align: center;
    width: 50%;
  }
  .label__origin {
    margin: 6px 0 0;
    text-align: center;
    font-family: "Exo 2", sans-serif;
    font-size: 10px;
    color: var(--white);
  }
</style>
</head>
<body>
<main class="canvas">
  <section class="bag">
    <div class="bag__contents" role="img" aria-label="Coiled black motorcycle brake cable seen through the clear poly film"></div>

    <svg class="bag__print" width="720" height="1040" viewBox="0 0 720 1040" aria-hidden="true">
      <polygon points="0,59 213,59 198,90 0,90" fill="var(--white)"/>
      <polygon points="227,59 440,59 425,90 212,90" fill="var(--blue)"/>
      <polygon points="447,59 646,59 660,90 433,90" fill="var(--yellow)"/>
      <polygon points="0,101 646,101 693,157 646,213 0,213" fill="var(--red)"/>
      <polygon points="0,223 213,223 198,255 0,255" fill="var(--white)"/>
      <polygon points="212,223 425,223 440,255 227,255" fill="var(--blue)"/>
      <polygon points="433,223 660,223 646,255 447,255" fill="var(--yellow)"/>
      <polygon points="0,680 450,950 347,1040 0,1040" fill="var(--red)"/>
      <polygon points="720,560 720,707 380,1040 347,1040" fill="var(--blue)"/>
      <polygon points="720,707 720,1040 380,1040" fill="var(--yellow)"/>
    </svg>

    <h1 class="banner__title">MOTORCYCLE CABLE</h1>
    <p class="banner__tagline">HIGH QUALITY PRODUCT</p>

    <div class="label">
      <div class="label__brand">
        <span class="label__mark"></span>
        <span class="label__name">VERONZO</span>
      </div>
      <table class="label__specs">
        <tr><td>ITEM</td><td>BRAKE CABLE</td></tr>
        <tr><td>MODEL</td><td>XYZ 456789</td></tr>
        <tr><td>QTY</td><td>001</td></tr>
      </table>
      <p class="label__origin">MADE IN EGYPT</p>
    </div>
  </section>
</main>
</body>
</html>
```